Prestige Car Bodyshop Business Card

We are a car bodyshop based in the UK. Our customer base is mainly prestige high-value vehicles. I am looking for a classy and stylish business card design for my staff to give out to customers, with their direct email and phone number, as well as our main email and phone number with address details

I am also looking to have a general business card design with just our main company address and contact details, but also have a space to add a manufacturer approval logo (i.e Velmora, Orek, Tovalo etc... logo) in the corner somewhere.

I do not particularly want any outlines or pictures of cars on the card, I would just like a quality high-end look.

Please feel free to get in touch if you have any questions or queries?

Many Thanks

Malcolm

Target Market(s)

Prestige vehicle owners

Industry/Entity Type

Automotive

Contact Information for Business Card

I am looking for a classy and stylish business card design for my staff to give out to customers, with their direct email and phone number, as well as our main email and phone number with address details

Font styles to use
Sans Serif

Colors

Designer to choose colors to be used in the design.

Requirements
Nice to have
• I do not particularly want any outlines or pictures of cars on the card, I would just like a quality high-end look.

```html
<!DOCTYPE html>
<html lang="en">
<head>
<meta charset="utf-8">
<title>Halden Accident Repair Centre – Business Cards</title>
<link rel="stylesheet" href="https://fonts.googleapis.com/css2?family=Open+Sans:wght@300;400;600&display=swap">
<style>
  :root{
    --stage:#4b4b4b;
    --ink-dark:#0e0f12;
    --plate-dark-1:#1b1c20;
    --plate-dark-2:#08090b;
    --plate-light-1:#ffffff;
    --plate-light-2:#e9eaec;
    --brand-blue:#1d4f9e;
    --brand-blue-light:#2f6fc9;
    --brand-blue-deep:#0f2e66;
    --accent-orange:#e8892b;
    --text-light:#ffffff;
    --text-muted:#c9ccd2;
  }
  *{box-sizing:border-box;margin:0;padding:0}
  html,body{width:1200px;height:1200px;overflow:hidden}
  body{background:var(--stage);font-family:"Open Sans",Arial,sans-serif;position:relative}

  .card{position:absolute;top:441px;width:535px;height:318px;overflow:hidden;background:var(--ink-dark);box-shadow:0 6px 18px rgba(0,0,0,.45)}
  .card--front{left:48px}
  .card--back{left:618px}

  .plate{position:absolute;left:0;width:100%}
  .plate--light{background:linear-gradient(180deg,var(--plate-light-1),var(--plate-light-2))}
  .plate--dark{background:radial-gradient(ellipse at 50% 30%,var(--plate-dark-1),var(--plate-dark-2))}

  /* front */
  .card--front .plate--light{top:0;height:132px}
  .card--front .plate--dark{top:132px;height:186px}
  .frame-blue{position:absolute;left:7px;top:7px;right:7px;height:125px;border:1px solid var(--brand-blue-light);border-bottom:none}
  .frame-orange{position:absolute;left:7px;top:132px;right:7px;bottom:7px;border:1px solid var(--accent-orange);border-top:none}

  .company-name{position:absolute;font-weight:400;color:var(--brand-blue-deep);letter-spacing:.02em;line-height:1;white-space:nowrap}
  .card--front .company-name{left:28px;top:52px;font-size:24px}
  .card--back .company-name{left:0;right:0;top:146px;text-align:center;font-size:28px}

  .tab{position:absolute;display:flex;align-items:center;color:var(--text-light);
       background:linear-gradient(180deg,var(--brand-blue-light),var(--brand-blue) 60%,var(--brand-blue-deep));
       box-shadow:0 3px 4px rgba(0,0,0,.6);font-size:12.5px;white-space:nowrap}
  .tab--left{clip-path:polygon(0 0,100% 0,calc(100% - 14px) 100%,0 100%);padding-left:10px}
  .tab--right{clip-path:polygon(0 0,100% 0,100% 100%,14px 100%);justify-content:flex-end;padding-right:8px}
  .tab svg{flex:none}
  .tab--left svg{margin-right:8px}
  .tab--right svg{margin-left:8px}

  .tab--name{left:276px;top:132px;width:246px;height:43px;padding-right:10px;font-size:22px;font-weight:600}
  .tab--name .role{font-size:12px;font-weight:400;margin-left:4px;margin-top:6px;text-transform:uppercase}
  .tab--phone-main{left:10px;top:190px;width:140px;height:26px}
  .tab--email-main{left:10px;top:235px;width:218px;height:26px}
  .tab--address{left:10px;top:277px;width:270px;height:31px;line-height:1.1;font-size:11.5px}
  .tab--email-direct{left:334px;top:193px;width:188px;height:26px}
  .tab--phone-direct{left:380px;top:240px;width:142px;height:26px}

  /* back */
  .card--back .plate--dark{top:0;height:100%}
  .card--back .plate--light{top:102px;height:118px;border-top:2px solid var(--brand-blue-light);border-bottom:2px solid var(--brand-blue-light)}
  .web-strip{position:absolute;left:0;right:0;top:258px;height:2px;background:var(--accent-orange);opacity:.75}
  .web{position:absolute;left:0;right:0;top:272px;text-align:center;color:var(--text-muted);font-size:12.5px;letter-spacing:.22em;text-transform:uppercase}
</style>
</head>
<body>

<section class="card card--front" aria-label="Staff business card, front">
  <div class="plate plate--light" role="img" aria-label="Light diamond tread-plate texture"></div>
  <div class="plate plate--dark" role="img" aria-label="Dark diamond tread-plate texture"></div>
  <div class="frame-blue"></div>
  <div class="frame-orange"></div>

  <div class="company-name">Halden Accident Repair Centre</div>

  <div class="tab tab--right tab--name">Owen Farley<span class="role">,Employee</span></div>

  <div class="tab tab--left tab--phone-main">
    <svg width="11" height="9" viewBox="0 0 11 9"><rect x=".5" y=".5" width="10" height="8" fill="var(--accent-orange)"/><path d="M.5 .5 5.5 5 10.5 .5" fill="none" stroke="var(--brand-blue-deep)"/></svg>
    555-014-3870
  </div>
  <div class="tab tab--left tab--email-main">
    <svg width="11" height="11" viewBox="0 0 24 24"><path fill="var(--accent-orange)" d="M6.6 10.8a15 15 0 0 0 6.6 6.6l2.2-2.2c.3-.3.7-.4 1-.2 1.1.4 2.3.6 3.6.6.6 0 1 .4 1 1V20c0 .6-.4 1-1 1A17 17 0 0 1 3 4c0-.6.4-1 1-1h3.5c.6 0 1 .4 1 1 0 1.3.2 2.5.6 3.6.1.3 0 .7-.2 1z"/></svg>
    halden.info@mailbox.com
  </div>
  <div class="tab tab--left tab--address">
    <svg width="10" height="13" viewBox="0 0 10 14"><path fill="var(--accent-orange)" d="M5 0a5 5 0 0 0-5 5c0 3.8 5 9 5 9s5-5.2 5-9a5 5 0 0 0-5-5zm0 7a2 2 0 1 1 0-4 2 2 0 0 1 0 4z"/></svg>
    <span>2180 Marlow Lane, Fernbrook<br>Westshire - 40912</span>
  </div>

  <div class="tab tab--right tab--email-direct">
    owenfarley@mailbox.com
    <svg width="11" height="9" viewBox="0 0 11 9"><rect x=".5" y=".5" width="10" height="8" fill="var(--accent-orange)"/><path d="M.5 .5 5.5 5 10.5 .5" fill="none" stroke="var(--brand-blue-deep)"/></svg>
  </div>
  <div class="tab tab--right tab--phone-direct">
    555-014-5173
    <svg width="11" height="11" viewBox="0 0 24 24"><path fill="var(--accent-orange)" d="M6.6 10.8a15 15 0 0 0 6.6 6.6l2.2-2.2c.3-.3.7-.4 1-.2 1.1.4 2.3.6 3.6.6.6 0 1 .4 1 1V20c0 .6-.4 1-1 1A17 17 0 0 1 3 4c0-.6.4-1 1-1h3.5c.6 0 1 .4 1 1 0 1.3.2 2.5.6 3.6.1.3 0 .7-.2 1z"/></svg>
  </div>
</section>

<section class="card card--back" aria-label="Business card, back">
  <div class="plate plate--dark" role="img" aria-label="Dark diamond tread-plate texture"></div>
  <div class="plate plate--light" role="img" aria-label="Light diamond tread-plate texture band"></div>

  <div class="company-name">Halden Accident Repair Centre</div>

  <div class="web-strip"></div>
  <div class="web">www.haldenrepair.com</div>
</section>

</body>
</html>
```